Health care startup that needs to WOW bone marrow doctors with presentation brochure

We need a brochure to compliment our in person presentation to Transplant Hospital Directors. The design needs to feel contemporary and clean. We need to convey a very professional operation that embraces technology. We want to break in as a modern company in an industry that has historically been non-profit and a little dull.

Our website is corvantix.com

I've included an early brochure we had from our site. We like our logo. The "Corvantix blue" in the logo is #7CD9DA in Microsoft Office products

I envision the brochure having two folds to reveal three pages. Ive added some of the text and images we will use.

The charts and graphs included in the attached ppt. can be modified by the designer but we want to capture the information in the final design.

Target Market(s)

Transplant Center Physicians

Industry/Entity Type

Healthcare

Colors
85cae6

Requirements
Must have
• a foldout brochure with at least three pages.
• Emphasis on our key competitive advantages, minority donors (80%), predominantly male (70%) and average age 21. This needs to be emphasized.
• I want to show that we will be a cost leader in the industry as well.
Nice to have
• I like the idea of a pocket or some means to attach a personal letter to clients on the inside. Not sure if that would work with the flow of the document.
• Websites whose design we LOVE:
• http://www.drelvonsuite.com/solutions/overview/
• http://quorelbay.com/
Should not have
• I dont want plain stock photos of people looking straight at a camera smiling. This feels like a non-profit trying to elict sympathy. Compassion for patients in a core value of the company, but it should still feel like something that is modern and new and a change to the current industry

```html
<!DOCTYPE html>
<html lang="en">
<head>
<meta charset="utf-8">
<title>Corvantix Brochure</title>
<link href="https://fonts.googleapis.com/css2?family=Open+Sans:wght@400;600;700&display=swap" rel="stylesheet">
<style>
:root{
  --bg:#d4d5d7;
  --paper:#ffffff;
  --teal:#9ad6dc;
  --teal-deep:#7ccdd4;
  --heading:#7fcfd6;
  --ink:#3c3c3c;
  --ink-soft:#555;
  --photo-a:#b7dfe3;
  --badge:#cfd6d9;
}
*{box-sizing:border-box;margin:0;padding:0}
html,body{width:1200px;height:1052px;overflow:hidden;background:var(--bg);font-family:"Open Sans",Arial,sans-serif;color:var(--ink)}
.canvas{position:relative;width:1200px;height:1052px}
.panel{position:absolute;background:var(--paper);overflow:hidden}
.abs{position:absolute}
.h-section{color:var(--heading);font-size:14px;font-weight:400;line-height:18px}
.body-copy{font-size:7.6px;line-height:10px;color:var(--ink)}
.dot-icon{position:absolute;width:11px;height:11px;border:1.5px solid var(--ink-soft);border-radius:50%}
.brand{display:flex;align-items:center;gap:6px;color:var(--ink);font-weight:400;letter-spacing:3px;line-height:1}
.brand-mark{border:1.5px solid var(--teal-deep);border-radius:50%}
.badge{position:absolute;background:var(--badge)}
.feature h4{color:var(--heading);font-size:10px;font-weight:600;margin-bottom:2px;line-height:13px}
.feature p{font-size:6.4px;line-height:8px;color:var(--ink)}
.feature .tick{position:absolute;left:-19px;top:2px;width:10px;height:10px}
.contact{text-align:center;font-size:10.5px;line-height:13px;color:var(--ink)}
.photo{position:absolute}
.highlight-list li{list-style:none;position:relative;padding-left:20px;font-size:7.6px;line-height:10px;margin-bottom:10px;color:var(--ink)}
.highlight-list li::before{content:"";position:absolute;left:0;top:1px;width:10px;height:10px;border:1.2px solid #8a8a8a;border-radius:50%}
.stat{position:absolute;background:var(--paper);text-align:center;box-shadow:1px 2px 3px rgba(0,0,0,.12)}
.stat b{display:block;color:var(--teal-deep);font-size:25px;font-weight:700;line-height:30px;margin-top:4px}
.stat span{display:block;font-size:10px;line-height:14px;color:var(--ink)}
.reg-list li{list-style:none;position:relative;padding-left:16px;font-size:7.4px;line-height:10px;color:var(--ink)}
.reg-list li::before{content:"";position:absolute;left:0;top:2px;width:7px;height:7px;border:1px solid var(--teal-deep);border-radius:50%}
.reg-list li.sub{padding-left:22px}
.reg-list li.sub::before{display:none}
.years li{margin-bottom:10px}
</style>
</head>
<body>
<div class="canvas">

  <!-- Inside spread, panel 1 -->
  <section class="panel" style="left:47px;top:43px;width:367px;height:476px">
    <span class="dot-icon" style="left:47px;top:53px"></span>
    <h2 class="h-section abs" style="left:75px;top:47px">Our Mission</h2>
    <p class="body-copy abs" style="left:75px;top:74px;width:250px">Corvantix believes that all bone marrow transplant patients should have a donor match delivered on time at an affordable price. To that end we are building a world class registry to aid Transplant Centers in treating their ethnic minority patients. We are committed to proving customer service excellence second to none.</p>
    <div class="brand abs" style="left:222px;top:168px;font-size:17px">
      <span class="brand-mark" style="width:16px;height:16px"></span>CORVANTIX
    </div>
    <span class="dot-icon" style="left:47px;top:210px;border-radius:2px"></span>
    <h2 class="h-section abs" style="left:75px;top:204px">What we Do</h2>
    <p class="body-copy abs" style="left:75px;top:233px;width:250px">As a total transplant procurement solution, Corvantix vertically integrates as a registry and donation center to maximize efficiency and provide operational excellence to deliver marrow/PBSCs on time - at industry leading prices. Corvantix harnesses industry leading best practices to target, recruit, and maintain active donors with unprecedented donor follow through rates. Transplant Center clients access these donors through our web based software, Helixa. Once identified as a potential match, Corvantix guides donors through CT, workup, and collection. We then personally deliver the product to our transplant center clients.</p>
    <span class="dot-icon" style="left:47px;top:389px"></span>
    <h2 class="h-section abs" style="left:75px;top:383px">Our Partners</h2>
    <div class="badge" style="left:73px;top:420px;width:65px;height:16px"></div>
    <div class="badge" style="left:143px;top:420px;width:60px;height:16px"></div>
    <div class="badge" style="left:212px;top:420px;width:65px;height:16px"></div>
    <div class="badge" style="left:285px;top:420px;width:55px;height:16px"></div>
  </section>

  <!-- Inside spread, panel 2 -->
  <section class="panel" style="left:414px;top:43px;width:367px;height:476px">
    <span class="abs" style="left:28px;top:56px;font-size:13px;font-weight:700;color:var(--ink);line-height:18px">??</span>
    <h2 class="h-section abs" style="left:56px;top:55px">Why Choose Corvantix</h2>
    <div class="feature abs" style="left:78px;top:94px;width:80px">
      <svg class="tick" viewBox="0 0 10 10"><circle cx="5" cy="5" r="4.2" fill="none" stroke="#555"/><path d="M3 5l1.6 1.6L7.5 3.4" fill="none" stroke="#555" stroke-width="1.2"/></svg>
      <h4>Efficient</h4><p>Increase donor availability from our domestically sourced registry; Reducing cycle time from donor contact to HCT/P delivery.</p>
    </div>
    <div class="feature abs" style="left:179px;top:94px;width:75px">
      <svg class="tick" viewBox="0 0 10 10"><circle cx="5" cy="5" r="4.2" fill="none" stroke="#555"/><circle cx="5" cy="5" r="1.6" fill="#555"/></svg>
      <h4>Targeted</h4><p>Donor base recruitment focusing on minority males (18-25 year old).</p>
    </div>
    <div class="feature abs" style="left:268px;top:94px;width:88px">
      <svg class="tick" viewBox="0 0 10 10"><circle cx="5" cy="5" r="4.2" fill="none" stroke="#555"/><path d="M5 2.5V5h2" fill="none" stroke="#555"/></svg>
      <h4>Responsive</h4><p>24/7 access to a personal Corvantix donation coordinator from initial match to HCT/P delivery.</p>
    </div>
    <div class="feature abs" style="left:78px;top:187px;width:80px">
      <svg class="tick" viewBox="0 0 10 10"><circle cx="5" cy="5" r="4.2" fill="none" stroke="#555"/><path d="M1 5h8M5 1v8" stroke="#555"/></svg>
      <h4>Intelligent</h4><p>Secure, intuitive website to easily search the Corvantix database and monitor donations in progress.</p>
    </div>
    <div class="feature abs" style="left:181px;top:187px;width:80px">
      <svg class="tick" viewBox="0 0 10 10"><circle cx="5" cy="3" r="2.2" fill="#555"/><path d="M1 10c0-3 2-4.5 4-4.5S9 7 9 10z" fill="#555"/></svg>
      <h4>Professional</h4><p>HCT/P transport provided by a dedicated Corvantix team member.</p>
    </div>
    <div class="abs" style="left:0;top:279px;width:367px;height:197px;background:var(--teal)">
      <div class="brand abs" style="left:138px;top:44px;font-size:17px">
        <span class="brand-mark" style="width:16px;height:16px;border-color:#555"></span>CORVANTIX
      </div>
      <p class="contact abs" style="left:0;width:367px;top:101px">Get Started Today</p>
      <p class="contact abs" style="left:0;width:367px;top:126px">Please contact us to learn more:<br>480 Larkspur Avenue, NW | Easton | DC | 20019<br>P 202.555.0147<br>www.corvantix.com</p>
    </div>
  </section>

  <!-- Cover -->
  <section class="panel" style="left:781px;top:43px;width:369px;height:476px">
    <div class="photo" role="img" aria-label="Soft flowing teal wave backdrop" style="left:0;top:0;width:369px;height:476px;background:radial-gradient(ellipse 140% 80% at 110% 100%,#7fd0d6 0%,#c4ebed 40%,#ffffff 70%)"></div>
    <div class="brand abs" style="left:52px;top:76px;font-size:23px">
      <span class="brand-mark" style="width:20px;height:20px"></span>CORVANTIX
    </div>
    <p class="abs" style="left:73px;top:152px;font-size:18.5px;line-height:22px;color:var(--ink)">The Solution to<br>Bone Marrrow<br><span style="color:var(--heading);font-weight:700">Donor Shortages</span></p>
    <p class="abs" style="right:41px;top:441px;font-size:11px;color:var(--ink)">www.corvantix.com</p>
  </section>

  <!-- Outside spread, panel 1 -->
  <section class="panel" style="left:47px;top:536px;width:367px;height:475px">
    <div class="photo" role="img" aria-label="Photo of clinicians reviewing records together, tinted teal" style="left:0;top:15px;width:367px;height:164px;background:linear-gradient(90deg,var(--photo-a),#a6d4da 60%,#c6e6e9)"></div>
    <h2 class="abs" style="left:46px;top:143px;font-size:21px;font-weight:400;color:#4a5a5e;line-height:28px">Highlights</h2>
    <ul class="highlight-list abs" style="left:58px;top:203px;width:240px">
      <li>100% domestically sourced donor base</li>
      <li>Emphasis on African Americans and Hispanic males in the 18-25 year old demographic</li>
      <li>Reduced cycle time resulting from our co-location strategy</li>
      <li>24/7 access to a designated Corvantix donation coordinator from confirmatory typing through delivery to Transplant Center</li>
      <li>Industry cost leader</li>
      <li>Secure, user friendly web site to easily access and search the Corvantix donor database and track the progress of current donations</li>
      <li>Courier service by Corvantix employees</li>
    </ul>
    <p class="abs" style="left:60px;top:442px;font-size:11px;color:var(--ink)">www.corvantix.com</p>
  </section>

  <!-- Outside spread, panel 2 -->
  <section class="panel" style="left:414px;top:536px;width:367px;height:475px;background:var(--teal)">
    <div class="photo" role="img" aria-label="Photo of a medical team discussing a chart, grey tint" style="left:0;top:15px;width:367px;height:164px;background:linear-gradient(90deg,#8b979c,#a0a9ad 50%,#b4bcbf)"></div>
    <p class="abs" style="left:45px;top:208px;font-size:14px;line-height:17px;color:#4a5a5e">Corvantix Registry<br>at Glance</p>
    <svg class="abs" style="left:179px;top:197px" width="156" height="137" viewBox="0 0 156 137" role="img" aria-label="Line chart of recruited donors from October to April">
      <rect width="156" height="137" fill="#fff"/>
      <text x="78" y="17" font-size="9" text-anchor="middle" fill="#333" font-family="Open Sans,sans-serif">Number of Recruited Donors</text>
      <g stroke="#999" stroke-width=".6">
        <line x1="40" y1="33" x2="146" y2="33"/><line x1="40" y1="52" x2="146" y2="52"/><line x1="40" y1="71" x2="146" y2="71"/><line x1="40" y1="90" x2="146" y2="90"/><line x1="40" y1="109" x2="146" y2="109"/>
      </g>
      <g font-size="6.5" fill="#333" text-anchor="end" font-family="Open Sans,sans-serif">
        <text x="35" y="35">2,000</text><text x="35" y="54">1,500</text><text x="35" y="73">1,000</text><text x="35" y="92">500</text><text x="35" y="111">0</text>
      </g>
      <polyline points="43,109 60,108.7 77,107 94,99 111,86 128,69 145,48" fill="none" stroke="#555" stroke-width="2"/>
      <g font-size="6.5" fill="#333" font-family="Open Sans,sans-serif">
        <text transform="translate(46,124) rotate(-55)">Oct</text><text transform="translate(63,124) rotate(-55)">Nov</text><text transform="translate(80,124) rotate(-55)">Dec</text><text transform="translate(97,124) rotate(-55)">Jan</text><text transform="translate(114,124) rotate(-55)">Feb</text><text transform="translate(131,127) rotate(-55)">March</text><text transform="translate(148,125) rotate(-55)">April</text>
      </g>
    </svg>
    <p class="abs" style="left:39px;top:339px;font-size:15px;line-height:17.5px;color:#4a5a5e">Donor<br>Ethnicity<br>Composition</p>
    <div class="stat" style="left:39px;top:397px;width:95px;height:54px"><b>80%</b><span>Ethnic Minorities</span></div>
    <div class="stat" style="left:147px;top:397px;width:88px;height:54px"><b>70%</b><span>Male</span></div>
    <div class="stat" style="left:249px;top:397px;width:86px;height:54px"><b>21%</b><span>Average Age</span></div>
  </section>

  <!-- Outside spread, panel 3 -->
  <section class="panel" style="left:781px;top:536px;width:369px;height:475px">
    <svg class="abs" style="left:0;top:0" width="369" height="475" aria-hidden="true"><polygon points="59,334 369,334 369,475 9,475" fill="var(--teal)"/></svg>
    <h2 class="abs" style="left:37px;top:14px;font-size:20px;font-weight:400;color:var(--ink);line-height:28px">Helixa</h2>
    <p class="abs" style="left:37px;top:47px;width:305px;font-size:7.4px;line-height:10px;color:var(--ink)">Transplant Centers match their patients to Corvantix donors on Helixa, developed by Veltrano, an Industry leader used in numerous international registries</p>
    <ul class="reg-list abs" style="left:37px;top:97px;width:152px">
      <li>Integration with Global Marrow Donor Network and Continental Donor Data Exchange (CDDX).</li>
      <li>Complies with International Marrow Donor Council</li>
      <li>Verified FDA compliant by independent consulting audit</li>
      <li><b style="font-weight:600">ISO accreditation requested by UKMR</b></li>
      <li class="sub">- 9001 (Quality Management System)</li>
      <li class="sub">- 27001 (Information Security Management System)</li>
      <li>SOPs, project plans</li>
      <li>Guarantees for testing, validation, security, etc.</li>
    </ul>
    <ul class="reg-list years abs" style="left:197px;top:99px;width:165px">
      <li><b style="font-weight:600">2007:</b> Czech Republic, Slovakia</li>
      <li><b style="font-weight:600">2008:</b> Cyprus, Bulgaria, Poland</li>
      <li><b style="font-weight:600">2009:</b> South Africa, Finland</li>
      <li><b style="font-weight:600">2010:</b> Sweden, Denmark, Slovenia, Israel</li>
      <li><b style="font-weight:600">2011:</b> Hungary, Argentina, Great Britain (UKMR), Belgium, Ireland, Saudi Arabia</li>
      <li><b style="font-weight:600">2012:</b> Nigeria, Cordlink, ...</li>
    </ul>
    <div class="badge" style="left:48px;top:287px;width:26px;height:24px;border-radius:50%"></div>
    <div class="badge" style="left:80px;top:287px;width:26px;height:24px;border-radius:50%"></div>
    <div class="badge" style="left:112px;top:287px;width:26px;height:24px;border-radius:50%"></div>
    <div class="badge" style="left:144px;top:290px;width:38px;height:18px"></div>
    <div class="badge" style="left:213px;top:252px;width:50px;height:16px"></div>
    <div class="badge" style="left:272px;top:252px;width:50px;height:16px"></div>
    <div class="badge" style="left:330px;top:249px;width:22px;height:22px;border-radius:50%"></div>
    <div class="badge" style="left:215px;top:283px;width:22px;height:26px"></div>
    <div class="badge" style="left:253px;top:285px;width:46px;height:22px"></div>
    <div class="badge" style="left:311px;top:283px;width:26px;height:26px"></div>
    <div class="badge" style="left:344px;top:284px;width:22px;height:24px"></div>
  </section>

</div>
</body>
</html>
```